Harbourline capital partners pty ltd

Hi guys I recently opened a brokerage company. I need a flyer to capture the attention of customers.
I would like something professional and cool at the same time.
My website is harbourcp.com.au
I also attached the current flyer. as you can see it lacks of originality and it isn't cool!!!!
Thank you

Target Market(s)

People between the age of 18-50

Industry/Entity Type

Financial Service

Requirements
Must have
• Mast have features and contents that reflects the website
• harbourcp.com.au
Nice to have
• Open to anything
Should not have
• Not to sure

```html
<!DOCTYPE html>
<html lang="en">
<head>
<meta charset="utf-8">
<title>Harbourline Capital Partners Pty Ltd – Flyer</title>
<link href="https://fonts.googleapis.com/css2?family=Montserrat:wght@300;400;500;600;700&display=swap" rel="stylesheet">
<style>
  :root{
    --blue:#2a9fd8;
    --orange:#f39021;
    --navy:#1c2530;
    --paper:#f2f2f2;
    --ink:#555a5f;
    --body:#43484d;
    --white:#ffffff;
  }
  *{margin:0;padding:0;box-sizing:border-box}
  html,body{width:948px;height:1200px;overflow:hidden;background:var(--paper)}
  body{font-family:"Montserrat",Arial,sans-serif;color:var(--body)}
  .flyer{position:relative;width:948px;height:1200px;overflow:hidden;background:var(--paper)}
  .shapes{position:absolute;inset:0}
  .brand{position:absolute;left:53px;top:58px;display:flex;align-items:center;gap:14px}
  .brand-mark{width:34px;height:34px;background:var(--blue)}
  .brand-name{font-size:25px;font-weight:500;color:var(--blue);line-height:1.15;letter-spacing:.5px;text-transform:uppercase}
  .headline{position:absolute;left:40px;top:612px;font-size:39px;line-height:44px;font-weight:600;color:var(--ink)}
  .headline .accent{display:block;color:var(--blue);font-weight:300;font-size:42px}
  .intro{position:absolute;left:40px;top:716px;width:511px;font-size:16.2px;line-height:18.6px;font-weight:400;text-align:justify;color:var(--body)}
  .specialise{position:absolute;left:40px;top:857px;font-size:26.5px;font-weight:600;color:var(--blue);letter-spacing:.5px}
  .services{position:absolute;left:40px;top:901px;display:grid;grid-template-columns:166px auto;row-gap:7px;list-style:none;font-size:19.5px;line-height:22px;color:var(--body)}
  .services li{display:flex;align-items:center;gap:9px}
  .services svg{width:16px;height:16px;flex:none}
  .side{position:absolute;left:625px;top:484px;width:298px}
  .side h2{font-size:25.5px;font-weight:600;color:var(--orange);line-height:30px}
  .side p{margin-top:6px;font-size:15px;line-height:18.4px;font-weight:300;text-align:justify;color:var(--body)}
  .side ul{list-style:none;font-size:15.5px;line-height:20.5px;font-weight:300;color:var(--body)}
  .lenders{margin-top:12px}
  .why{margin-top:24px}
  .reasons{margin-top:6px}
  .contact{position:absolute;left:40px;top:1118px;list-style:none;font-size:16.5px;line-height:21px;color:var(--white);font-weight:400}
  .contact li{display:flex;align-items:center;gap:8px}
  .contact svg{width:13px;height:13px;flex:none}
</style>
</head>
<body>
<main class="flyer">
  <svg class="shapes" viewBox="0 0 948 1200" width="948" height="1200">
    <defs>
      <linearGradient id="photoTone" x1="0" y1="0" x2="1" y2="1">
        <stop offset="0" stop-color="#1d2f3e"/>
        <stop offset=".45" stop-color="#3c5670"/>
        <stop offset=".75" stop-color="#6f8aa6"/>
        <stop offset="1" stop-color="#4a5f75"/>
      </linearGradient>
    </defs>
    <rect class="hero-photo" x="0" y="0" width="948" height="600" fill="url(#photoTone)" role="img" aria-label="Photo of a silver-blue sports coupe driving along a coastal road"/>
    <path class="wave-white" d="M0 538 C280 430 640 385 948 455 L948 1200 L0 1200 Z" fill="var(--white)"/>
    <path class="wave-orange" d="M0 556 C280 450 640 405 948 470 L948 1200 L0 1200 Z" fill="var(--orange)"/>
    <path class="wave-paper" d="M0 614 C300 475 640 435 948 478 L948 1200 L0 1200 Z" fill="var(--paper)"/>
    <path class="footer-band" d="M0 993 L620 1135 C760 1110 880 1040 948 973 L948 1200 L0 1200 Z" fill="var(--navy)"/>
    <path class="footer-white" d="M660 1160 C790 1120 890 1060 948 1005 L948 1200 Z" fill="var(--white)"/>
    <path class="footer-orange" d="M729 1152 C820 1118 900 1072 948 1038 L948 1200 Z" fill="var(--orange)"/>
  </svg>

  <div class="brand">
    <span class="brand-mark"></span>
    <span class="brand-name">Harbourline Capital<br>Partners Pty Ltd</span>
  </div>

  <h1 class="headline">It’s time to finance<span class="accent">Your Dream</span></h1>

  <p class="intro">Harbourline capital partners is a bespoke brokerage firm established by a team of professionals who bring with them over 50 year’s combined experience in consulting, finance, negotiation, and executive roles within the finance and automotive industry. We strive for excellence, delivering the right solution for our clients in a timely and professional manner.</p>

  <h2 class="specialise">WE SPECIALISE IN FINANCING</h2>
  <ul class="services">
    <li><svg viewBox="0 0 16 16"><circle cx="8" cy="8" r="7" fill="none" stroke="var(--blue)" stroke-width="1.4"/><path d="M4.6 8.2l2.3 2.3 4.5-4.6" fill="none" stroke="var(--blue)" stroke-width="1.5"/></svg>Cars</li>
    <li><svg viewBox="0 0 16 16"><circle cx="8" cy="8" r="7" fill="none" stroke="var(--blue)" stroke-width="1.4"/><path d="M4.6 8.2l2.3 2.3 4.5-4.6" fill="none" stroke="var(--blue)" stroke-width="1.5"/></svg>Jet skis</li>
    <li><svg viewBox="0 0 16 16"><circle cx="8" cy="8" r="7" fill="none" stroke="var(--blue)" stroke-width="1.4"/><path d="M4.6 8.2l2.3 2.3 4.5-4.6" fill="none" stroke="var(--blue)" stroke-width="1.5"/></svg>Boats</li>
    <li><svg viewBox="0 0 16 16"><circle cx="8" cy="8" r="7" fill="none" stroke="var(--blue)" stroke-width="1.4"/><path d="M4.6 8.2l2.3 2.3 4.5-4.6" fill="none" stroke="var(--blue)" stroke-width="1.5"/></svg>Trucks</li>
    <li><svg viewBox="0 0 16 16"><circle cx="8" cy="8" r="7" fill="none" stroke="var(--blue)" stroke-width="1.4"/><path d="M4.6 8.2l2.3 2.3 4.5-4.6" fill="none" stroke="var(--blue)" stroke-width="1.5"/></svg>Caravans</li>
    <li><svg viewBox="0 0 16 16"><circle cx="8" cy="8" r="7" fill="none" stroke="var(--blue)" stroke-width="1.4"/><path d="M4.6 8.2l2.3 2.3 4.5-4.6" fill="none" stroke="var(--blue)" stroke-width="1.5"/></svg>Earth moving Equipment</li>
  </ul>

  <aside class="side">
    <h2>Our Financiers include</h2>
    <p>We have privileged and specialized access to a wide range of lenders enabling us to tailor solutions which cater to your individual needs. We work with:</p>
    <ul class="lenders">
      <li>• Ashcombe Finance</li>
      <li>• Larkspan Leasing</li>
      <li>• Velmora Finance</li>
      <li>• Brindlewood Finance</li>
      <li>• Pimbrook Asset finance</li>
      <li>• Orrindale Motor Finance</li>
      <li>• Fenwick and General Finance</li>
      <li>• Corvell Finance</li>
      <li>• Quillon Finance</li>
    </ul>
    <h2 class="why">Why use us</h2>
    <ul class="reasons">
      <li>• Low rates</li>
      <li>• Access Australia’s most<br>trusted lenders</li>
      <li>• Quick &amp; easy, same day approvals</li>
      <li>• Professional advice</li>
      <li>• New, Used, private or dealer sale<br>- the choice is yours</li>
      <li>• 100% Finance available</li>
    </ul>
  </aside>

  <ul class="contact">
    <li><svg viewBox="0 0 14 14"><path d="M3 1.5l2 .3.8 2.6-1.3 1a7 7 0 0 0 3.9 3.9l1-1.3 2.6.8.3 2c-.4.9-1.3 1.3-2.2 1.2A10.5 10.5 0 0 1 1.8 3.7c-.1-.9.3-1.8 1.2-2.2z" fill="var(--orange)"/></svg>+61 400 123 987</li>
    <li><svg viewBox="0 0 14 14"><rect x="1" y="3" width="12" height="8" rx="1" fill="none" stroke="var(--orange)" stroke-width="1.4"/><path d="M1.5 3.8L7 7.8l5.5-4" fill="none" stroke="var(--orange)" stroke-width="1.4"/></svg>admin@harbourcp.com.au</li>
    <li><svg viewBox="0 0 14 14"><circle cx="7" cy="7" r="5.8" fill="none" stroke="var(--orange)" stroke-width="1.3"/><ellipse cx="7" cy="7" rx="2.5" ry="5.8" fill="none" stroke="var(--orange)" stroke-width="1.1"/><path d="M1.3 7h11.4" stroke="var(--orange)" stroke-width="1.1"/></svg>www.harbourcp.com.au</li>
  </ul>
</main>
</body>
</html>
```